Zielgruppe
Ich bin Selfpublisher und habe eine Lust Wunschzettel als Buch kreiert. Die Zielgruppe sind meist junge Erwachsene, aber auch welche mittleren alters.
Aufgabenstellung
Titel des Buches: Der dicke LUST WUNSCHZETTEL
Untertitel: 150 Orte +10 eigene Orte für mehr Nervenkitzel und Erlebnisse
Der Anfang vom Titel 'Die große' kann ruhig sehr klein abgebildet werden.
Das Wort 'SEX' im Titel soll am größten auf dem Cover sein und auch bei kleinster Darstellung gut sichtbar und sehr prägnant sein.
Der Teil vom Untertitel '+10 eigene Orte für mehr Nervenkitzel und Erlebnisse' kann ruhig getrennt von den '150 Orten' stehen.
In dem Buch sind 150 Orte plus jeweils Felder zum Ankreuzen und beschreiben vorhanden, wie der Sex dort war.
Farben: Die Hauptfarbe soll ins rote gehen.
Auf keinen Fall darf dieses Rot #EE3A43 benutzt werden, da dies die Farbe eines Mitbewerbers ist.
Hier zwei Beispiele welche Farben benutzt werden können: #FF4D8D, #FF6686. Natürlich sind auch andere und ähnliche Farben in Ordnung. Dies diente nur zur Orientierung, wie weit das Rot verändert werden muss.
Es sollen keine echten Fotos verwendet werden. Außerdem sollen keine Menschen, oder Illustrationen von Menschen abgebildet werden.
Ich habe eine Datei hochgeladen, worin sich mehrere Illustrationen befinden. Die können in der Farbe und vom Aussehen verändert werden. Das benutzen der Illustrationen ist absolut kein muss! Ich lasse mich gerne von anderen Designs überraschen.
Mit den Illustrationen könnte man zum Beispiel sowas wie auf dem Cover der 'Onkel Tourenheft' abgebildet machen. Bild ist im Anhang. Hierfür müssen die Illustrationen (Sex Icons) mit passenden Farben versehen werden. Es sollte nicht zu Bunt werden, also hier 3-4 Farben aussuchen.
Außerdem eventuell ein Schrift Effekt wie bei dem Titel der 'Garden Quest' auch im Anhang zu finden. Natürlich gehen auch andere passende Effekte. Hier kenne ich mich nicht aus, was so möglich ist.
Es sollte allgemein nicht zu langweilig sein. Etwas Dynamik und Effekte sind gut. Wie bei den bereits genannten Beispiel Covern.

```html
<!DOCTYPE html>
<html lang="de">
<head>
<meta charset="utf-8">
<title>Lust Wunschzettel – Buchcover</title>
<link rel="stylesheet" href="https://fonts.googleapis.com/css2?family=Archivo+Black&family=Oswald:wght@600&display=swap">
<style>
  :root {
    --backdrop: #d9dbda;
    --cover-pink: #ec6580;
    --cover-pink-dark: #c05068;
    --paper: #ffffff;
  }
  html, body {
    margin: 0;
    padding: 0;
    width: 1200px;
    height: 1200px;
    overflow: hidden;
    background: var(--backdrop);
  }
  .book-cover {
    position: absolute;
    left: 200px;
    top: 0;
    width: 800px;
    height: 1200px;
    background: var(--cover-pink);
    overflow: hidden;
  }
  .cover-art {
    position: absolute;
    inset: 0;
  }
  .title-main {
    position: absolute;
    left: 124px;
    top: 508px;
    width: 640px;
    margin: 0;
    font-family: "Archivo Black", "Arial Black", sans-serif;
    font-weight: 400;
    font-size: 118px;
    line-height: 122px;
    color: var(--paper);
    letter-spacing: -2px;
    white-space: nowrap;
  }
  .title-main span { display: block; }
  .subtitle {
    position: absolute;
    left: 254px;
    top: 850px;
    margin: 0;
    font-family: "Oswald", "Arial Narrow", sans-serif;
    font-weight: 600;
    color: var(--paper);
    text-transform: uppercase;
  }
  .subtitle-count {
    display: block;
    font-size: 60px;
    line-height: 66px;
    letter-spacing: -0.5px;
  }
  .subtitle-extra {
    display: block;
    font-size: 30px;
    line-height: 42px;
    letter-spacing: -0.3px;
  }
  .author-band {
    position: absolute;
    left: 0;
    bottom: 0;
    width: 800px;
    height: 93px;
    background: var(--paper);
    display: flex;
    align-items: center;
    justify-content: center;
  }
  .author-name {
    margin: 0;
    font-family: "Archivo Black", "Arial Black", sans-serif;
    font-size: 42px;
    letter-spacing: 2px;
    color: var(--cover-pink);
    text-transform: uppercase;
  }
</style>
</head>
<body>
  <main class="book-cover">
    <svg class="cover-art" width="800" height="1200" viewBox="0 0 800 1200" xmlns="http://www.w3.org/2000/svg">
      <path fill="var(--cover-pink-dark)"
            d="M92 150 L72 158 Q72 158 72 180 L72 455 Q72 475 95 473 L509 440 L525 506 L604 445 L674 440 Q690 438 690 420 L690 410 L92 460 Z"/>
      <path fill="var(--paper)"
            d="M120 127 L682 88 Q709 87 709 110 L709 375 Q709 395 682 398 L598 402 L509 479 L509 410 L119 444 Q92 446 92 422 L92 152 Q92 129 120 127 Z"/>
      <text x="398" y="345" text-anchor="middle" transform="rotate(-5 398 290)"
            font-family="Archivo Black, Arial Black, sans-serif" font-size="190"
            fill="var(--cover-pink)" letter-spacing="-4">LUST</text>
      <path fill="var(--cover-pink-dark)" d="M603 835 L701 844 L708 852 L610 843 Z"/>
      <path fill="var(--paper)"
            d="M513 786 Q555 748 600 753 Q665 760 671 841 L701 844 L645 924 L603 835 L631 837 Q627 790 590 775 Q550 762 513 786 Z"/>
      <ellipse cx="525" cy="946" rx="34" ry="5" fill="var(--cover-pink-dark)"/>
      <path fill="var(--paper)"
            d="M525 847 A33 33 0 0 1 556 893 L528 941 Q525 945 522 941 L494 893 A33 33 0 0 1 525 847 Z"/>
      <circle cx="525" cy="880" r="13" fill="var(--cover-pink)"/>
    </svg>

    <h1 class="title-main"><span>WUNSCH</span><span>ZETTEL</span></h1>

    <p class="subtitle">
      <span class="subtitle-count">150 Orte</span>
      <span class="subtitle-extra">+10 eigene Orte</span>
      <span class="subtitle-extra">für mehr Nervenkitzel</span>
      <span class="subtitle-extra">und Erlebnisse</span>
    </p>

    <footer class="author-band">
      <p class="author-name">Jorven Hallmark</p>
    </footer>
  </main>
</body>
</html>
```